The Wardrobe Sage needs a pricing flyer

Single page flyer for The Wardrobe Sage.
The Wardrobe Sage is a lead generation service exclusively for the custom closet industry.
You design quality closets we provide quality leads!
Value Points:
Leads for closet companies are exclusive with a first right of refusal. Meaning, if the closet company cannot handle all of the leads we can provide, we will sell the excess to other closet companies. We will never sell the same lead to two different closet companies.
Benefits:
Flat rate and easy to budget
Cancel at anytime
Choose from 3 types of leads
Lower cost compared to overall cost per lead from other sources
More leads allows hiring more designers
More leads grow the companies revenue
Less time managing other advertising models
3 service options.
$250 each
- We send you the lead
- You and your team set the appointment
- Setting the appointment is up to you
2. $275 each
- We send you the lead
- We guarantee the appointment
- Return unset appointments for a replacement
3. $375 each
- We are your call center
- We generate the lead
- We set the appointment
Contact:
The Wardrobe Sage
704-555-0183
leads@TheWardrobeSage.com
Look and feel
Each slider illustrates characteristics of the customer's brand and the style your logo design should communicate.

```html
<!DOCTYPE html>
<html lang="en">
<head>
<meta charset="utf-8">
<title>The Wardrobe Sage – Pricing Flyer</title>
<link href="https://fonts.googleapis.com/css2?family=Libre+Baskerville:wght@400;700&family=Montserrat:wght@400;500;600&display=swap" rel="stylesheet">
<style>
  :root{
    --cream:#fbf1e8;
    --blush:#f4e1d3;
    --brown:#9b5a2e;
    --peach:#f7c79a;
    --ink:#3b2a20;
    --text:#5a4436;
    --white:#fffaf5;
  }
  *{margin:0;padding:0;box-sizing:border-box}
  html,body{width:896px;height:1200px;overflow:hidden}
  body{background:#e9e2dc;font-family:"Montserrat",sans-serif;color:var(--text)}
  .flyer{position:relative;width:896px;height:1200px;overflow:hidden;
    background:linear-gradient(160deg,var(--cream) 0%,var(--blush) 55%,#f1d8c5 100%)}
  .brand{position:absolute;left:80px;top:50px;width:300px;text-align:center}
  .brand-mark{width:20px;height:20px;border-radius:50%;background:var(--brown);margin:0 auto 14px}
  .brand-name{font-family:"Libre Baskerville",serif;font-weight:400;font-size:40px;line-height:1.15;color:var(--brown)}
  .headline{position:absolute;left:455px;top:45px;width:413px;height:255px;background:var(--brown);
    padding:30px 28px;font-family:"Libre Baskerville",serif;font-size:38px;line-height:1.2}
  .headline .lead{color:var(--white);display:block}
  .headline .accent{color:var(--peach);display:block}
  .section-title{font-family:"Libre Baskerville",serif;font-size:28px;color:var(--brown);margin-bottom:8px}
  .value{position:absolute;left:60px;top:320px;width:370px}
  .value p{font-size:14px;line-height:1.45;color:var(--text)}
  .benefits{position:absolute;left:95px;top:530px;width:340px;height:330px;background:var(--brown);padding:20px 24px}
  .benefits .section-title{color:var(--white);font-size:26px}
  .benefits ul{list-style:none}
  .benefits li{position:relative;padding-left:22px;font-size:14px;line-height:1.35;color:var(--white);margin-bottom:5px}
  .benefits li::before{content:"";position:absolute;left:2px;top:6px;width:7px;height:7px;background:var(--peach);transform:rotate(45deg)}
  .photo-showroom{position:absolute;left:460px;top:305px;width:400px;height:390px;
    background:linear-gradient(135deg,#c9a58a 0%,#7a5845 45%,#3e2c24 100%);
    clip-path:polygon(50% 0,100% 50%,50% 100%,0 50%)}
  .photo-cabinet{position:absolute;left:60px;top:872px;width:375px;height:298px;
    background:linear-gradient(160deg,#7c8590 0%,#4a525c 60%,#c2b3a2 100%);
    clip-path:polygon(12% 0,88% 0,100% 18%,100% 100%,0 100%,0 18%)}
  .services{position:absolute;left:480px;top:700px;width:385px}
  .services .section-title{font-size:28px;margin-bottom:6px}
  .tier{margin-bottom:8px}
  .tier h3{font-family:"Libre Baskerville",serif;font-weight:400;font-size:15px;color:var(--ink);margin-bottom:2px}
  .tier ul{list-style:none}
  .tier li{position:relative;padding-left:20px;font-size:13.5px;line-height:19px;color:var(--text)}
  .tier li::before{content:"";position:absolute;left:2px;top:6px;width:7px;height:7px;background:var(--brown);transform:rotate(45deg)}
  .contact{position:absolute;left:450px;top:1040px;width:418px;height:125px;background:var(--brown);padding:16px 26px;color:var(--white)}
  .contact h2{font-family:"Libre Baskerville",serif;font-weight:400;font-size:19px;margin-bottom:10px}
  .contact-row{display:flex;align-items:center;gap:10px;font-size:14px;margin-bottom:6px}
  .contact-row svg{flex:none}
</style>
</head>
<body>
<main class="flyer">
  <header class="brand">
    <div class="brand-mark"></div>
    <div class="brand-name">The Wardrobe Sage</div>
  </header>

  <section class="headline">
    <span class="lead">You Design Quality Closets</span>
    <span class="accent">We Provide Quality Leads!</span>
  </section>

  <section class="value">
    <h2 class="section-title">Value Points</h2>
    <p>Leads for closet companies are exclusive with a first right of refusal. Meaning, if the closet company cannot handle all of the leads we can provide, we will sell the excess to other closet companies. We will never sell the same lead to two different closet companies.</p>
  </section>

  <div class="photo-showroom" role="img" aria-label="Photo of a designer standing in a warm, well-lit custom walk-in closet"></div>

  <section class="benefits">
    <h2 class="section-title">Benefits</h2>
    <ul>
      <li>Flat rate and easy to Budget</li>
      <li>Cancel at Anytime</li>
      <li>Choose From 3 Types of Leads</li>
      <li>Lower Cost compared to Overall Cost Per Lead from other Sources</li>
      <li>More Leads Allows Hiring more Designers</li>
      <li>More Leads Grow the Companies Revenue</li>
      <li>Less Time Managing Other Advertising Models</li>
    </ul>
  </section>

  <div class="photo-cabinet" role="img" aria-label="Photo of grey custom closet cabinetry with a chair"></div>

  <section class="services">
    <h2 class="section-title">Service Options</h2>
    <div class="tier">
      <h3>$250 Each</h3>
      <ul>
        <li>We send you the lead</li>
        <li>You and your team set the appointment</li>
        <li>Setting the appointment is up to you</li>
      </ul>
    </div>
    <div class="tier">
      <h3>$275 Each</h3>
      <ul>
        <li>We send you the lead</li>
        <li>You and your team set the appointment</li>
        <li>We guarantee the appointment</li>
        <li>Return unset appointments for a replacement</li>
      </ul>
    </div>
    <div class="tier">
      <h3>$375 Each</h3>
      <ul>
        <li>We are your call center</li>
        <li>We generate the lead</li>
        <li>We set the appointment</li>
      </ul>
    </div>
  </section>

  <section class="contact">
    <h2>Reach Us!</h2>
    <div class="contact-row">
      <svg width="15" height="15" viewBox="0 0 24 24"><path fill="#fffaf5" d="M6.6 10.8a15 15 0 006.6 6.6l2.2-2.2c.3-.3.7-.4 1-.2 1.1.4 2.3.6 3.6.6.6 0 1 .4 1 1V20c0 .6-.4 1-1 1A17 17 0 013 4c0-.6.4-1 1-1h3.5c.6 0 1 .4 1 1 0 1.3.2 2.5.6 3.6.1.3 0 .7-.2 1z"/></svg>
      <span>704-555-0183</span>
    </div>
    <div class="contact-row">
      <svg width="15" height="15" viewBox="0 0 24 24"><path fill="#fffaf5" d="M3 5h18v14H3z"/><path fill="none" stroke="#9b5a2e" stroke-width="2" d="M3 6l9 7 9-7"/></svg>
      <span>leads@TheWardrobeSage.com</span>
    </div>
  </section>
</main>
</body>
</html>
```